Upscale business cards needed for family business

We need professional business cards created for several family members. We are a family business holding company. We would like these relatively simple and straightforward, but also with a unique element to set them apart. Probably stick with neutral and simple colors - white, grey etc. We need space for the traditional elements, including name, title, address, email/phone number. And we will be creating several from this template so it needs to be template that is easy to switch information in and out of.

Industry/Entity Type

Business

Contact Information for Business Card

Please include the attached Dunmore Ventures logo.

Requirements
Must have
• The attached Dunmore Ventures logo.

```html
<!DOCTYPE html>
<html lang="en">
<head>
<meta charset="utf-8">
<title>Dunmore Ventures Business Card</title>
<link rel="stylesheet" href="https://fonts.googleapis.com/css2?family=Cinzel:wght@500;600&family=Open+Sans:wght@400&display=swap">
<style>
  :root {
    --page-bg: #3a3a3a;
    --card-white: #ffffff;
    --card-black: #131617;
    --ink: #1e1e1e;
    --ink-soft: #4a4a4a;
    --gold: #c9982c;
    --gold-light: #f0c230;
    --gold-dark: #a8782a;
    --white: #ffffff;
  }
  html, body {
    margin: 0;
    padding: 0;
    width: 1105px;
    height: 1200px;
    overflow: hidden;
    background: var(--page-bg);
  }
  .canvas {
    position: relative;
    width: 1105px;
    height: 1200px;
  }
  .card {
    position: absolute;
    left: 192px;
    width: 720px;
    height: 412px;
    overflow: hidden;
  }
  .card-front { top: 146px; background: var(--card-white); }
  .card-back  { top: 602px; background: var(--card-black); }

  .brand {
    position: absolute;
    font-family: "Cinzel", serif;
    font-weight: 500;
    white-space: nowrap;
    margin: 0;
  }
  .card-front .brand {
    top: 118px;
    left: 342px;
    width: 318px;
    text-align: center;
    font-size: 27px;
    color: var(--ink);
  }
  .card-back .brand {
    top: 220px;
    left: 0;
    width: 720px;
    text-align: center;
    font-size: 40px;
    color: var(--white);
  }

  .person-name {
    position: absolute;
    top: 208px;
    left: 40px;
    margin: 0;
    font-family: "Cinzel", serif;
    font-weight: 600;
    font-size: 29px;
    letter-spacing: 1px;
    color: var(--gold);
  }
  .person-title {
    position: absolute;
    top: 245px;
    left: 40px;
    margin: 0;
    font-family: "Open Sans", sans-serif;
    font-size: 19px;
    color: var(--ink);
  }
  .divider {
    position: absolute;
    top: 277px;
    left: 40px;
    width: 639px;
    height: 2px;
    background: var(--ink);
  }
  .contact, .address {
    position: absolute;
    top: 290px;
    margin: 0;
    padding: 0;
    list-style: none;
    font-family: "Open Sans", sans-serif;
    font-size: 18px;
    line-height: 27px;
    color: var(--ink-soft);
    font-style: normal;
  }
  .contact { left: 40px; }
  .contact li { display: flex; align-items: center; gap: 10px; }
  .contact svg { width: 18px; height: 18px; fill: var(--gold); flex: none; }
  .address { right: 41px; text-align: right; }

  .gold-band {
    position: absolute;
    left: 0;
    bottom: 0;
    width: 400px;
    height: 16px;
    background: linear-gradient(90deg, var(--gold-dark), var(--gold-light) 75%, var(--gold));
  }
  .web-tab {
    position: absolute;
    right: 0;
    bottom: 0;
    width: 330px;
    height: 46px;
  }
  .web-tab svg { position: absolute; inset: 0; }
  .web-tab span {
    position: absolute;
    right: 20px;
    top: 9px;
    font-family: "Open Sans", sans-serif;
    font-size: 19px;
    letter-spacing: 2px;
    color: var(--white);
  }

  .back-url {
    position: absolute;
    top: 336px;
    left: 0;
    width: 720px;
    text-align: center;
    margin: 0;
    font-family: "Open Sans", sans-serif;
    font-size: 19px;
    letter-spacing: 1.5px;
    color: var(--white);
  }
</style>
</head>
<body>
<main class="canvas">

  <section class="card card-front" aria-label="Business card front">
    <p class="brand">Dunmore Ventures Inc</p>

    <h1 class="person-name">Daniel Reyes</h1>
    <p class="person-title">CEO/Founder</p>
    <div class="divider"></div>

    <ul class="contact">
      <li>
        <svg viewBox="0 0 24 24" aria-hidden="true"><path d="M6.6 10.8c1.4 2.8 3.8 5.1 6.6 6.6l2.2-2.2c.3-.3.7-.4 1-.2 1.1.4 2.3.6 3.6.6.6 0 1 .4 1 1V20c0 .6-.4 1-1 1C10.6 21 3 13.4 3 4c0-.6.4-1 1-1h3.5c.6 0 1 .4 1 1 0 1.3.2 2.5.6 3.6.1.3 0 .7-.2 1l-2.3 2.2z"/></svg>
        555 214 7790
      </li>
      <li>
        <svg viewBox="0 0 24 24" aria-hidden="true"><path d="M2 5h20v14H2z M2 5l10 8 10-8" fill="none" stroke="#c9982c" stroke-width="0"/><path d="M2 6.5l10 7 10-7V19H2z"/><path d="M2 5h20l-10 7z"/></svg>
        daniel@dunmoreventures.com
      </li>
    </ul>

    <address class="address">
      2140 Alder Court<br>
      Juneau, Alaska 99801
    </address>

    <div class="gold-band"></div>
    <div class="web-tab">
      <svg viewBox="0 0 330 46" preserveAspectRatio="none" aria-hidden="true">
        <path d="M0 46 C6 14 18 0 48 0 L330 0 L330 46 Z" fill="var(--card-black)"/>
      </svg>
      <span>www.dunmoreventures.com</span>
    </div>
  </section>

  <section class="card card-back" aria-label="Business card back">
    <p class="brand">Dunmore Ventures Inc</p>
    <p class="back-url">www.dunmoreventuresinc.com</p>
  </section>

</main>
</body>
</html>
```